Handmade clothes, homewares and fashion accessories

I need a business card for my new company that crochets, knits and sews homewares, fashion accessories and clothing. I would like a soft cream coloured background (maybe, or a colour scheme that you would think would compliment the graphics) with a funky designed robin sitting down with her feet forward and gently tangled up with a ball of wool and a bobbin of cotton, one either side of her. I would like the robin to have the classic red breast and to be looking happy.
Updates
Hi everyone
Sorry to be a pain, but I think I would like the design to be unisex as my previous one was too female orientated. Thanks

Hi everyone
I am leaning more towards a teal colour scheme with the robin being the feature and a more neutral font, not so feminine. Thanks

Target Market(s)
Females of all ages
Industry/Entity Type
Fashion
Contact Information for Business Card
Velvet Heron
Handmade in Larkmoor Mossbank Region
Moira Fenwick PO Box 317 Larkmoor MR 4821
Look and feel
Each slider illustrates characteristics of the customer's brand and the style your logo design should communicate.

```html
<!DOCTYPE html>
<html lang="en">
<head>
<meta charset="utf-8">
<title>Velvet Heron – Business Card</title>
<link rel="stylesheet" href="https://fonts.googleapis.com/css2?family=Fondamento&display=swap">
<style>
  :root {
    --page-bg: #eceded;
    --burlap-light: #d9b98a;
    --burlap-mid: #c49a64;
    --burlap-dark: #8f6a3e;
    --panel-cream: #fbeccd;
    --ink: #2f2a26;
    --accent-red: #c8202c;
    --art-brown: #a4856a;
  }
  html, body {
    margin: 0;
    width: 1200px;
    height: 802px;
    overflow: hidden;
    background: var(--page-bg);
  }
  .canvas {
    position: relative;
    width: 1200px;
    height: 802px;
    font-family: "Fondamento", Georgia, serif;
    color: var(--ink);
  }
  .card {
    position: absolute;
    left: 136px;
    top: 119px;
    width: 903px;
    height: 541px;
    overflow: hidden;
  }
  .burlap {
    position: absolute;
    inset: 0;
    background: radial-gradient(ellipse at center, var(--burlap-light) 0%, var(--burlap-mid) 70%, var(--burlap-dark) 100%);
  }
  .panel {
    position: absolute;
    left: 78px;
    top: 72px;
    width: 754px;
    height: 410px;
    background: var(--panel-cream);
    border-radius: 4px;
    box-shadow: 0 0 6px rgba(120, 85, 40, 0.35);
  }
  .mascot-art {
    position: absolute;
    left: 115px;
    top: 95px;
    width: 296px;
    height: 270px;
    border-radius: 40% 40% 30% 30%;
    background: radial-gradient(circle at 40% 35%, var(--art-brown) 0%, #c9ad8e 45%, rgba(216, 50, 58, 0.55) 75%, rgba(251, 236, 205, 0) 100%);
  }
  .brand-name {
    position: absolute;
    left: 120px;
    top: 372px;
    margin: 0;
    font-size: 38px;
    font-weight: 400;
    color: var(--accent-red);
    line-height: 1;
  }
  .tagline {
    position: absolute;
    right: 136px;
    top: 412px;
    margin: 0;
    font-size: 29px;
    color: var(--accent-red);
    line-height: 1;
  }
  .contact {
    position: absolute;
    right: 132px;
    top: 102px;
    text-align: right;
    font-size: 26px;
  }
  .contact p { margin: 0; }
  .contact .person { font-size: 25px; line-height: 34px; margin-bottom: 12px; }
  .contact .phone { font-size: 31px; line-height: 36px; margin-bottom: 30px; }
  .contact .address-line { line-height: 34px; }
  .icon {
    display: inline-block;
    vertical-align: -2px;
    margin-right: 20px;
  }
  .phone .icon { margin-right: 6px; }
</style>
</head>
<body>
<div class="canvas">
  <div class="card">
    <div class="burlap" role="img" aria-label="Woven burlap fabric texture"></div>
    <div class="panel"></div>
    <div class="mascot-art" role="img" aria-label="Illustration of a cartoon robin sitting tangled in red yarn between a cotton bobbin and a ball of wool"></div>

    <p class="brand-name">Velvet Heron</p>
    <p class="tagline">Handmade in Larkmoor</p>

    <div class="contact">
      <p class="person">Moira Fenwick</p>
      <p class="phone">
        <svg class="icon" width="22" height="24" viewBox="0 0 24 24" aria-hidden="true"><path fill="#2f2a26" d="M6.6 10.8a15.1 15.1 0 0 0 6.6 6.6l2.2-2.2c.3-.3.7-.4 1-.2 1.1.4 2.3.6 3.6.6.6 0 1 .4 1 1V20c0 .6-.4 1-1 1A17 17 0 0 1 3 4c0-.6.4-1 1-1h3.5c.6 0 1 .4 1 1 0 1.3.2 2.5.6 3.6.1.3 0 .7-.2 1z"/></svg>01 5550 2841
      </p>
      <p class="address-line">
        <svg class="icon" width="24" height="20" viewBox="0 0 24 20" aria-hidden="true"><path fill="#2f2a26" d="M12 1 1 8h3v11h16V8h3zM7 10h10v7H7z"/></svg>Mossbank Region
      </p>
      <p class="address-line">PO Box 317</p>
      <p class="address-line">Larkmoor MR 4821</p>
    </div>
  </div>
</div>
</body>
</html>
```